Kestrel Chiropractic Clinic Design

I am a Chiropractor and I treat a lot of conditions ranging from aches and pains to arthritis and nervous system issues. I would like a professional looking card with my logo and all of the other information that I have provided up top. I do like working with athletes (runners, football players, crossfit, and sports of that nature) so that is one aspect of my practice that varies from some of the others in town. My goal is to get patients out of pain and back to living their lives and doing what they love.

I would like to have a grey background also. Most of my marketing banners and things have the logo on a grey background and I would like to stick with that if possible.
Updates

Hello Everyone,

So one of the things that I wanted was a Grey background for the logo. All of my other marketing things have the logo on a grey background (pantone color 428C). If I could get that color on both the front and the back of the card I would appreciate it. I don't care if the card has white on it I just want my logo sitting on the grey color if possible.

Target Market(s)

really just everyone with emphasis on Athletes ranging from 18-35 years old

Industry/Entity Type

Marketing

Contact Information for Business Card

Kestrel Chiropractic Clinic
Dr. Wesley Marlow
4718 Hollow Brook, Suite 300
Fairview Springs, KS 66012
phone= 555-812-3961
fax= 555-812-7045
email= kestrelchiroclinic@mailbox.example

Requirements
Must have
• I must have my logo present

```html
<!DOCTYPE html>
<html lang="en">
<head>
<meta charset="utf-8">
<title>Kestrel Chiropractic Clinic – Business Card</title>
<link rel="stylesheet" href="https://fonts.googleapis.com/css2?family=Ubuntu:wght@400;500&family=Roboto+Condensed:wght@400;700&display=swap">
<style>
  :root {
    --stage: #d9d6d1;
    --card-light: #fbfbfb;
    --card-shade: #e6e6e6;
    --brand-blue: #0b5fa8;
    --brand-green: #2ea344;
    --ink-blue: #1358a0;
  }
  * { box-sizing: border-box; margin: 0; padding: 0; }
  html, body {
    width: 1200px; height: 800px; overflow: hidden;
    background: var(--stage);
  }
  .stage {
    width: 1200px; height: 800px;
    display: flex; align-items: center; justify-content: center;
  }
  .card {
    position: relative;
    width: 1000px; height: 571px;
    background: radial-gradient(ellipse at 55% 45%, var(--card-light) 0%, #f1f1f1 55%, var(--card-shade) 100%);
    overflow: hidden;
    box-shadow: 0 6px 24px rgba(0,0,0,.18);
  }
  .band { position: absolute; left: 0; width: 100%; height: 26px; display: block; }
  .band--top { top: 10px; }
  .band--bottom { bottom: 12px; }

  .card__name {
    position: absolute; left: 72px; top: 118px;
    font-family: "Ubuntu", sans-serif; font-weight: 400;
    font-size: 34px; letter-spacing: .5px; color: var(--ink-blue);
    white-space: nowrap;
  }
  .brand {
    position: absolute; left: 120px; top: 222px;
    display: flex; align-items: center; gap: 14px;
    white-space: nowrap;
  }
  .brand__dot {
    width: 20px; height: 20px; border-radius: 50%;
    background: var(--brand-green);
  }
  .brand__name {
    font-family: "Ubuntu", sans-serif; font-weight: 400;
    font-size: 42px; color: var(--brand-blue); letter-spacing: .5px;
  }
  .contact {
    position: absolute; left: 150px; top: 330px;
    font-family: "Roboto Condensed", sans-serif; font-size: 26px;
    border-collapse: collapse; white-space: nowrap;
  }
  .contact th {
    text-align: left; font-weight: 700; color: var(--brand-green);
    padding: 2px 22px 2px 0; vertical-align: top;
  }
  .contact td { color: var(--ink-blue); padding: 2px 0; }
</style>
</head>
<body>
<main class="stage">
  <article class="card">
    <svg class="band band--top" viewBox="0 0 1000 26" preserveAspectRatio="none" aria-hidden="true">
      <polygon points="0,0 575,0 555,26 0,26" fill="#0b5fa8"/>
      <polygon points="595,0 1000,0 1000,26 575,26" fill="#2ea344"/>
    </svg>

    <h1 class="card__name">Dr. Wesley Marlow</h1>

    <div class="brand">
      <span class="brand__dot"></span>
      <span class="brand__name">Kestrel Chiropractic Clinic</span>
    </div>

    <table class="contact">
      <tr><th>Add.:</th><td>4718 Hollow Brook, Suite 300 Fairview Springs, KS 66012</td></tr>
      <tr><th>Ph.:</th><td>555-812-3961</td></tr>
      <tr><th>Fax:</th><td>555-812-7045</td></tr>
      <tr><th>Email:</th><td>kestrelchiroclinic@mailbox.example</td></tr>
    </table>

    <svg class="band band--bottom" viewBox="0 0 1000 26" preserveAspectRatio="none" aria-hidden="true">
      <polygon points="0,0 520,0 500,26 0,26" fill="#2ea344"/>
      <polygon points="540,0 1000,0 1000,26 520,26" fill="#0b5fa8"/>
    </svg>
  </article>
</main>
</body>
</html>
```